Heron Accord Business Card

Need a business card for my nonprofit, Heron Accord Inc. Heron Accord is a conflict resolution practice that offers services that help people resolve problems peacefully.

Got Conflict? Try Conflict Coaching. Initial consultation is complimentary

Marisol Daventry-Kuhl, PhD
Heron Accord Inc.
www.heronaccord-example.org
E: info@heronaccord-example.org
P: 555-318-4927

Would like the attached logo on it, as well as our slogan, which is Finding Calm Around the RoomĀ®

```html
<!DOCTYPE html>
<html lang="en">
<head>
<meta charset="utf-8">
<title>Heron Accord Business Card</title>
<link href="https://fonts.googleapis.com/css2?family=Open+Sans:wght@400;600;700&display=swap" rel="stylesheet">
<style>
  :root {
    --stage: #383838;
    --card-white: #ffffff;
    --brand-red: #ec1c24;
    --brand-gold: #c9a23a;
    --ink: #333333;
    --petal-soft: #fbe3e5;
    --petal-red: #f04a4f;
  }
  * { margin: 0; padding: 0; box-sizing: border-box; }
  html, body { width: 1200px; height: 900px; overflow: hidden; }
  body {
    background: var(--stage);
    font-family: "Open Sans", Arial, sans-serif;
    position: relative;
  }
  .card {
    position: absolute;
    width: 477px;
    height: 294px;
    overflow: hidden;
    box-shadow: 2px 4px 8px rgba(0,0,0,0.45);
  }
  .card--front {
    left: 120px; top: 275px;
    background: var(--card-white);
    border-radius: 0 52px 0 52px;
  }
  .card--back {
    left: 607px; top: 273px;
    background: var(--brand-red);
    border-radius: 52px 0 52px 0;
  }
  .motif {
    position: absolute;
    border-radius: 50%;
  }
  .card--front .motif--top { right: -30px; top: 10px; width: 170px; height: 140px;
    background: radial-gradient(circle, var(--petal-soft) 0%, rgba(251,227,229,0) 70%); }
  .card--front .motif--bottom { left: -30px; bottom: -20px; width: 170px; height: 150px;
    background: radial-gradient(circle, var(--petal-soft) 0%, rgba(251,227,229,0) 70%); }
  .card--back .motif--top { right: -40px; top: 10px; width: 160px; height: 150px;
    background: radial-gradient(circle, var(--petal-red) 0%, rgba(240,74,79,0) 70%); }
  .card--back .motif--bottom { left: -40px; bottom: -30px; width: 150px; height: 150px;
    background: radial-gradient(circle, var(--petal-red) 0%, rgba(240,74,79,0) 70%); }

  .brand-name {
    position: absolute;
    font-weight: 600;
    text-transform: uppercase;
    line-height: 1.05;
  }
  .card--front .brand-name {
    left: 32px; top: 52px;
    color: var(--brand-gold);
    font-size: 38px;
    letter-spacing: 2px;
  }
  .card--back .brand-name {
    left: 0; right: 0; top: 96px;
    text-align: center;
    color: var(--card-white);
    font-size: 46px;
    letter-spacing: 3px;
  }
  .holder {
    position: absolute;
    left: 207px; top: 183px;
    font-size: 14px;
    font-weight: 700;
    color: var(--brand-red);
    text-transform: uppercase;
  }
  .holder .credential { color: var(--brand-gold); font-weight: 400; font-size: 12px; }
  .contact-list {
    position: absolute;
    left: 207px; top: 214px;
    list-style: none;
    font-size: 14px;
    color: var(--ink);
    line-height: 17.5px;
  }
  .contact-list li { display: flex; align-items: center; gap: 4px; }
  .contact-list svg { width: 12px; height: 12px; fill: var(--brand-red); }
  .divider {
    position: absolute;
    left: 115px; top: 217px;
    width: 245px; height: 1px;
    background: var(--card-white);
  }
  .slogan {
    position: absolute;
    left: 0; right: 0; top: 238px;
    text-align: center;
    color: var(--card-white);
    font-size: 13px;
    text-transform: uppercase;
  }
</style>
</head>
<body>
  <section class="card card--front">
    <div class="motif motif--top" role="img" aria-label="Faint decorative petal motif"></div>
    <div class="motif motif--bottom" role="img" aria-label="Faint decorative petal motif"></div>
    <div class="brand-name">Heron Accord</div>
    <p class="holder">Marisol Daventry-Kuhl<span class="credential">, PHD</span></p>
    <ul class="contact-list">
      <li><svg viewBox="0 0 12 12"><path d="M1 4c0-2 2-3 5-3s5 1 5 3v1H8.5V4h-5v1H1zM3 6h6l1.5 5h-9z"/></svg>555-318-4927</li>
      <li><svg viewBox="0 0 12 12"><path d="M1 3h10v6H1z M1 3l5 4 5-4" stroke="#fff" stroke-width="0.8"/></svg>info@heronaccord-example.org</li>
      <li><svg viewBox="0 0 12 12"><circle cx="6" cy="6" r="5"/></svg>www.heronaccord-example.org</li>
    </ul>
  </section>

  <section class="card card--back">
    <div class="motif motif--top" role="img" aria-label="Faint decorative petal motif"></div>
    <div class="motif motif--bottom" role="img" aria-label="Faint decorative petal motif"></div>
    <div class="brand-name">Heron Accord</div>
    <div class="divider"></div>
    <p class="slogan">Finding Calm Around the Room®</p>
  </section>
</body>
</html>
```